Lumenfield Holdings

Professional looking business card using darker colours
I do not yet have a logo for the company so feel free to suggest
The business is based on consultancy and project management
Based in Melbourne
Business card can omit the word "Holdings" and can be Lumenfield consulting etc.

Business

Contact Name on card : Tom Verisco Contact number : +61412 305 617 Email address will be confirmed shortly.

```html
<!DOCTYPE html>
<html lang="en">
<head>
<meta charset="utf-8">
<title>Lumenfield Consulting – Business Card</title>
<link href="https://fonts.googleapis.com/css2?family=Arimo:wght@400;700&family=Open+Sans:wght@400&family=Roboto+Condensed:wght@400&display=swap" rel="stylesheet">
<style>
  :root {
    --page: #ffffff;
    --label: #333333;
    --ink: #000000;
    --gold: #d8c27c;
    --gold-line: #c9ad5e;
    --navy: #0a0a4e;
    --violet: #3a00f5;
    --purple: #7a00f5;
    --white: #ffffff;
    --muted: #e6e6e6;
  }
  * { box-sizing: border-box; margin: 0; padding: 0; }
  html, body { width: 942px; height: 1200px; overflow: hidden; background: var(--page); }
  .sheet { position: relative; width: 942px; height: 1200px; }

  .side-label {
    position: absolute;
    font-family: "Open Sans", sans-serif;
    font-size: 31px;
    color: var(--label);
    word-spacing: 18px;
  }
  .side-label--front { left: 68px; top: 16px; }
  .side-label--back { left: 38px; top: 613px; }

  .card { position: absolute; left: 14px; width: 911px; overflow: hidden; }
  .card--front { top: 76px; height: 522px; background: var(--ink); }
  .card--back { top: 660px; height: 515px; background: linear-gradient(100deg, var(--navy) 0%, #1c00a8 45%, var(--violet) 100%); }
  .card svg.backdrop { position: absolute; inset: 0; }

  .brand-dot {
    position: absolute; border-radius: 50%;
    background: var(--gold);
  }
  .card--front .brand-dot { left: 100px; top: 78px; width: 104px; height: 104px; }

  .wordmark {
    position: absolute; left: 281px; top: 70px;
    font-family: "Arimo", sans-serif; font-weight: 700;
    color: var(--gold); line-height: 1;
  }
  .wordmark__name { display: block; font-size: 62px; letter-spacing: 2px; }
  .wordmark__tag { display: block; font-size: 22px; letter-spacing: 3px; margin-top: 10px; text-align: right; }

  .contact { position: absolute; left: 557px; top: 248px; color: var(--muted); }
  .contact__name { font-family: "Arimo", sans-serif; font-weight: 700; font-size: 32px; }
  .contact__line { font-family: "Roboto Condensed", sans-serif; font-size: 29px; margin-top: 8px; }

  .card--back .brand-dot { left: 214px; top: 220px; width: 60px; height: 60px; }
  .back-name {
    position: absolute; left: 184px; top: 292px; width: 120px; text-align: center;
    font-family: "Arimo", sans-serif; font-weight: 700; font-size: 16px; color: var(--white);
  }
  .divider { position: absolute; left: 321px; top: 213px; width: 2px; height: 130px; background: var(--white); }
  .services {
    position: absolute; left: 342px; top: 232px;
    font-family: "Arimo", sans-serif; font-weight: 700; font-size: 40px;
    line-height: 50px; color: var(--white);
  }
</style>
</head>
<body>
<div class="sheet">
  <div class="side-label side-label--front">Front B</div>

  <section class="card card--front">
    <svg class="backdrop" width="911" height="522" viewBox="0 0 911 522" aria-hidden="true">
      <defs>
        <linearGradient id="frontBand" x1="0" y1="0" x2="1" y2="0">
          <stop offset="0" stop-color="#0a0a4e"/>
          <stop offset="0.55" stop-color="#2a00d8"/>
          <stop offset="0.8" stop-color="#4200ff"/>
          <stop offset="1" stop-color="#7a00f5"/>
        </linearGradient>
        <linearGradient id="frontSheen" x1="0" y1="0" x2="1" y2="0">
          <stop offset="0" stop-color="#4a4128"/>
          <stop offset="1" stop-color="#1a170e"/>
        </linearGradient>
      </defs>
      <path d="M0 459 C100 488 220 480 400 440 S780 345 911 338 L911 522 L0 522 Z" fill="url(#frontBand)"/>
      <path d="M0 459 C100 488 220 480 400 440 S780 345 911 338" fill="none" stroke="var(--gold-line)" stroke-width="4"/>
    </svg>
    <svg class="backdrop" width="911" height="522" viewBox="0 0 911 522" role="img" aria-label="Fine gold wave-line pattern sweeping across the lower left">
      <path d="M0 268 C180 258 330 330 520 412 C460 428 420 436 400 440 C220 480 100 488 0 455 Z" fill="url(#frontSheen)" opacity="0.8"/>
    </svg>

    <div class="brand-dot" aria-hidden="true"></div>
    <h1 class="wordmark">
      <span class="wordmark__name">LUMENFIELD</span>
      <span class="wordmark__tag">CONSULTING</span>
    </h1>
    <svg class="backdrop" width="911" height="522" viewBox="0 0 911 522" aria-hidden="true">
      <line x1="282" y1="175" x2="646" y2="175" stroke="var(--gold-line)" stroke-width="4"/>
    </svg>

    <div class="contact">
      <p class="contact__name">Tom Verisco</p>
      <p class="contact__line">T: +61412 305 617</p>
      <p class="contact__line">Email:</p>
    </div>
  </section>

  <div class="side-label side-label--back">Back B</div>

  <section class="card card--back">
    <svg class="backdrop" width="911" height="515" viewBox="0 0 911 515" role="img" aria-label="Faint violet wave-line pattern across the lower card">
      <defs>
        <linearGradient id="backSheen" x1="0" y1="0" x2="1" y2="0">
          <stop offset="0" stop-color="#3a30c8"/>
          <stop offset="1" stop-color="#5a40ff"/>
        </linearGradient>
      </defs>
      <path d="M0 325 C260 300 480 460 911 385 L911 502 C480 550 260 426 0 433 Z" fill="url(#backSheen)" opacity="0.25"/>
    </svg>
    <div class="brand-dot" aria-hidden="true"></div>
    <p class="back-name">Lumenfield</p>
    <div class="divider" aria-hidden="true"></div>
    <h2 class="services">Business Consultancy<br>And Management</h2>
  </section>
</div>
</body>
</html>
```